Wordpress theme for new e-commerce tropical furniture manufacturing business

We want to develop a Wordpress theme to suit our new Reefline Furniture website currently under development, business details as below.
Please see attached logo design for ideas of the design. This logo will be used as - letterhead, business cards, furniture labels etc.
We are a small Australian family business that provides products as below:
- Hand Crafted, Creative Tropical design Furniture,
(manufacture and sales).
- Specializing in mirror- wall art
- One off – designs 'made to order'.
- Individually badged pieces, each with an identification production number.
Materials used that may be incorporated in the 'web theme designs' are: Bamboo, Wood, Waves, Ocean, Shells, Tropical flowers (eg; Hibiscus, Frangipani, Heliconias, Stralitzias), Palms,Pandanus & Stone etc. etc.
Industry/Entity Type
E-Commerce
Colors
Designer to choose colors to be used in the design.
Look and feel
Each slider illustrates characteristics of the customer's brand and the style your logo design should communicate.

```html
<!DOCTYPE html>
<html lang="en">
<head>
<meta charset="utf-8">
<title>Reefline Furniture — Shop</title>
<link href="https://fonts.googleapis.com/css2?family=Open+Sans:wght@300;400;600;700&family=Oswald:wght@300;400&family=Arimo:wght@700&display=swap" rel="stylesheet">
<style>
:root{
  --blue:#4e8ee8;
  --navy:#0f3a7a;
  --olive:#636c47;
  --link:#3a52e0;
  --accent:#1a8fd8;
  --ink:#333;
  --muted:#666;
  --slider:#e4e4e4;
  --footer:#2f2f2f;
  --footer-box:#383838;
  --btn:#1e1e1e;
  --sale:#e0157e;
}
*{box-sizing:border-box;margin:0;padding:0}
html,body{width:960px;height:1200px;overflow:hidden;background:#fff}
body{position:relative;font-family:"Open Sans",Arial,sans-serif;color:var(--ink)}
.abs{position:absolute}
.topbar{left:0;top:0;width:960px;height:20px;background:#f7f7f7;font-size:10px;color:#555;line-height:20px}
.topbar .left{left:18px}
.topbar .right{right:63px}
.brand{left:20px;top:42px;display:flex;align-items:center;gap:8px}
.brand-dot{width:18px;height:18px;border-radius:50%;background:var(--accent)}
.brand-name{font-size:19px;font-weight:600;color:var(--accent);letter-spacing:.5px}
.callout{left:727px;top:43px;font-size:13.5px;color:var(--accent);line-height:18px}
.navband{left:0;top:113px;width:960px;height:49px;background:var(--olive)}
.navline{left:0;top:161px;width:960px;height:3px;background:var(--blue)}
.nav{left:447px;top:108px;width:450px;height:54px;background:var(--blue);display:flex}
.nav a{font-family:"Oswald",sans-serif;font-weight:300;color:#fff;font-size:12.5px;text-decoration:none;height:54px;line-height:54px;text-align:center;border-right:1px solid rgba(255,255,255,.25)}
.nav a:last-child{border-right:0}
.slider{left:0;top:164px;width:960px;height:338px;background:radial-gradient(ellipse at 45% 40%,#f2f2f2,#dadada)}
.slide-art{left:176px;top:48px;width:275px;height:275px;border-radius:50%;background:radial-gradient(circle at 45% 40%,#f4f4f4 0 28%,#2a52d8 30%,#1536a8 70%,#dcdcdc 72%)}
.divider{left:480px;top:52px;width:1px;height:232px;background:#c9c9c9}
.slide-title{left:509px;top:62px;font-family:"Arimo",sans-serif;font-weight:700;font-size:39px;color:#333;letter-spacing:.5px}
.slide-title span{color:var(--navy)}
.slide-sub{left:511px;top:114px;font-size:17px;font-weight:300;color:#666}
.slide-text{left:511px;top:143px;width:230px;font-size:6.6px;line-height:11.2px;color:#777}
.slide-price{left:510px;top:200px;font-size:15px;color:#333}
.slide-price small{font-family:"Oswald",sans-serif;font-weight:300;font-size:14px;color:#555}
.slide-btn{left:511px;top:237px;width:65px;height:20px;background:var(--navy);color:#fff;font-size:7px;line-height:20px;text-align:center}
.dots{left:428px;top:308px;display:flex;gap:11px}
.dots i{width:12px;height:12px;border-radius:50%;background:#111;display:block}
.dots i.on{background:var(--blue)}
.results{left:18px;top:543px;font-size:10px;color:#666}
.sort{left:761px;top:543px;width:135px;height:16px;border:1px solid #999;font-family:Arial,sans-serif;font-size:10px;line-height:14px;padding-left:4px;color:#111}
.sort b,.sortbox b{position:absolute;right:5px;top:0;font-size:8px}
.sortbox{left:912px;top:535px;width:19px;height:16px;border:1px solid #999;border-top:0}
.card{top:581px;width:195px}
.thumb{width:195px;height:194px;box-shadow:0 1px 3px rgba(0,0,0,.25)}
.t-lamp{background:linear-gradient(90deg,#f0f0f0,#e8e8e8 60%,#f4f4f4)}
.t-black{background:radial-gradient(circle at 45% 45%,#3a3a3a 0 30%,#fff 55%)}
.t-blue{background:radial-gradient(circle at 50% 40%,#23a9c4 0 28%,#fff 50%)}
.t-stools{background:linear-gradient(90deg,#e2231a 0 35%,#6a3048 35% 65%,#4d3e45 65%)}
.card h3{font-family:"Oswald",sans-serif;font-weight:300;font-size:14.5px;color:#333;margin-top:17px}
.price{font-size:10px;color:var(--link);margin-top:9px}
.price s{color:#999;margin-right:2px}
.btn{margin-top:8px;width:91px;height:28px;background:var(--btn);border:1px solid #000;color:#555;font-size:10px;font-weight:700;line-height:26px;text-align:center}
.price.gap{margin-top:25px}
.sale{left:446px;top:576px;width:32px;height:32px;border-radius:50%;background:var(--sale);color:#fff;font-size:9px;font-weight:700;line-height:32px;text-align:center}
.pager{left:476px;top:927px;display:flex;border:1px solid #333}
.pager span{width:22px;height:21px;font-size:9px;line-height:21px;text-align:center;border-right:1px solid #333;color:#333}
.pager span:last-child{border-right:0}
.pager .cur{background:var(--blue);color:#fff}
.footer{left:0;top:994px;width:960px;height:206px;background:var(--footer)}
.footer h4{position:absolute;top:40px;font-family:"Oswald",sans-serif;font-weight:400;font-size:13px;color:#fff;letter-spacing:2px}
.blog{left:69px;top:70px;width:269px}
.blog a{display:block;font-size:10px;color:var(--link);text-decoration:none;height:38px;line-height:28px;border-bottom:1px solid #4a4a4a;margin-bottom:10px}
.blog a:last-child{border:0}
.comments{left:372px;top:71px;width:270px}
.comments div{height:39px;background:var(--footer-box);margin-bottom:8px;font-size:10px;color:#fff;line-height:39px;padding-left:12px}
.comments a{color:var(--link)}
.about{left:678px;top:70px;width:272px;font-size:10px;line-height:18.4px;color:#fff}
.about p+p{margin-top:9px}
</style>
</head>
<body>
<div class="abs topbar">
  <span class="abs left">Email: sales@reeflinemail.com &nbsp;| &nbsp;Toll free: 021 - 555 -0192</span>
  <span class="abs right">0 items - $0.00 | Login / Register</span>
</div>

<div class="abs brand"><span class="brand-dot"></span><span class="brand-name">Reefline Furniture</span></div>
<div class="abs callout">CALL NOW: (400) 555-0147<br>EMAIL : INFO@REEFLINE.COM</div>

<div class="abs navband"></div>
<div class="abs navline"></div>
<nav class="abs nav">
  <a style="width:73px">Home</a><a style="width:97px">About Us</a><a style="width:82px">Portfolio</a><a style="width:59px">Blog</a><a style="width:71px">Shop</a><a style="width:68px">Contact Us</a>
</nav>

<section class="abs slider">
  <div class="abs slide-art" role="img" aria-label="Blue round lounge chair with white cushion"></div>
  <div class="abs divider"></div>
  <h1 class="abs slide-title">RED <span>CHAIR</span></h1>
  <div class="abs slide-sub">ATTRACTIVE ROUND CHAIR</div>
  <p class="abs slide-text">Praesent sed lacus elit. Pellentesque habitant morbi tristique senectus et netus et malesuada fames ac turpis egestas. Sed vel fermentum sem. Nulla pharetra, sem vitae molestie venenatis, ipsum turpis interdum metus, at tempor odio justo vitae ante.</p>
  <div class="abs slide-price"><small>FROM</small> $560.99</div>
  <div class="abs slide-btn">SHOP NOW</div>
  <div class="abs dots"><i></i><i></i><i class="on"></i></div>
</section>

<div class="abs results">Showing 1–12 of 13 results</div>
<div class="abs sort">Default sorting<b>▼</b></div>
<div class="abs sortbox"><b>▼</b></div>

<div class="abs card" style="left:53px">
  <div class="thumb t-lamp" role="img" aria-label="Red shade floor lamp"></div>
  <h3>Bed lamp</h3><div class="price">$29.00</div><div class="btn">Add to cart</div>
</div>
<div class="abs card" style="left:280px">
  <div class="thumb t-black" role="img" aria-label="Black easy chair on chrome base"></div>
  <h3>Black Easy Chair</h3><div class="price gap"><s>$99.00</s> $49.00</div><div class="btn">Add to cart</div>
</div>
<div class="abs sale">Sale!</div>
<div class="abs card" style="left:507px">
  <div class="thumb t-blue" role="img" aria-label="Turquoise swivel chair"></div>
  <h3>Blue Chair</h3><div class="price">$150.00</div><div class="btn">Add to cart</div>
</div>
<div class="abs card" style="left:738px">
  <div class="thumb t-stools" role="img" aria-label="Red and purple upholstered stools"></div>
  <h3>Comfort Chairs</h3><div class="price">$50.00</div><div class="btn">Add to cart</div>
</div>

<div class="abs pager"><span class="cur">1</span><span>2</span><span>→</span></div>

<footer class="abs footer">
  <h4 style="left:69px">FRESH FROM THE BLOG</h4>
  <h4 style="left:372px">RECENT COMMENTS</h4>
  <h4 style="left:678px">ABOUT</h4>
  <div class="abs blog"><a>Hello world!</a><a>Responsive Theme</a><a>Unique Interior Models</a></div>
  <div class="abs comments">
    <div>marella on <a>Black Easy Chair</a></div>
    <div>marella on <a>Gray Easy Chair</a></div>
    <div>marella on <a>Sofa set</a></div>
  </div>
  <div class="abs about">
    <p>Wesce sit amet porttitor leo this is hyper link Cum sociis natoque penatibus et magnis dis parturient montes, nascetur ridiculus mus. Quisque interdum, nulla sit amet varius dignissim Vestibulum pretium risus</p>
    <p>Wesce sit amet porttitor leo this is hyper link Cum sociis natoque penatibus et magnis dis parturient.</p>
  </div>
</footer>
</body>
</html>
```